Business Card Design

Very plain simple card, Plain modern font. Background. Grey fading to black. Large Bright lime green text. Saying.

TWR-ZA.COM

Small other details in white text.

Irish Horse Sales . Livery . Stud . Shows

Mark Dabrowski
TWR
Birch Lodge
Carrowmede Lane
Thistlecombe
Lincolnshire
LN4 7JX

Email. Twrzap@mailvale.co.uk
Tel. 07482 936504

Industry/Entity Type

Business

Contact Information for Business Card

As below

```html
<!DOCTYPE html>
<html lang="en">
<head>
<meta charset="utf-8">
<title>TWR-ZA.COM Business Card</title>
<link rel="stylesheet" href="https://fonts.googleapis.com/css2?family=Rosario:wght@400;500&display=swap">
<style>
  :root {
    --page-bg: #05050a;
    --card-top: #4a4a4a;
    --card-mid: #262626;
    --card-bottom: #1b1b1b;
    --band: #111111;
    --lime: #a4c436;
    --art-green: #7aa332;
    --text-white: #f4f4f4;
  }
  * { box-sizing: border-box; margin: 0; padding: 0; }
  html, body {
    width: 1200px;
    height: 1000px;
    overflow: hidden;
    background: var(--page-bg);
    font-family: "Rosario", sans-serif;
  }
  .business-card {
    position: absolute;
    left: 243px;
    top: 295px;
    width: 715px;
    height: 410px;
    background: linear-gradient(to bottom, var(--card-top) 0%, var(--card-mid) 45%, var(--card-bottom) 75%, var(--card-bottom) 100%);
    overflow: hidden;
    color: var(--text-white);
  }
  .rider-art {
    position: absolute;
    left: 55px;
    top: 13px;
    width: 277px;
    height: 245px;
    display: block;
  }
  .brand-name {
    position: absolute;
    left: 300px;
    width: 410px;
    top: 128px;
    text-align: center;
    font-size: 37px;
    font-weight: 400;
    letter-spacing: 0.5px;
    color: var(--lime);
  }
  .services {
    position: absolute;
    left: 300px;
    width: 414px;
    top: 185px;
    text-align: center;
    font-size: 19px;
  }
  .contact-name {
    position: absolute;
    left: 300px;
    width: 414px;
    top: 228px;
    text-align: center;
    font-size: 24px;
  }
  .contact-band {
    position: absolute;
    left: 28px;
    top: 292px;
    width: 670px;
    height: 108px;
    border-radius: 40px;
    background: var(--band);
  }
  .contact-lines,
  .address {
    position: absolute;
    font-size: 17.5px;
    line-height: 30px;
    font-style: normal;
  }
  .contact-lines { left: 62px; top: 305px; line-height: 27px; }
  .address { left: 343px; top: 294px; }
</style>
</head>
<body>
  <main class="business-card">
    <svg class="rider-art" viewBox="0 0 277 245" role="img" aria-label="Line illustration of a jockey riding a galloping horse in lime green">
      <defs>
        <radialGradient id="riderGlow" cx="50%" cy="50%" r="55%">
          <stop offset="0%" stop-color="#7aa332" stop-opacity="0.55"/>
          <stop offset="100%" stop-color="#7aa332" stop-opacity="0.15"/>
        </radialGradient>
      </defs>
      <rect width="277" height="245" rx="20" fill="url(#riderGlow)"/>
    </svg>

    <h1 class="brand-name">TWR-ZA.COM</h1>
    <p class="services">Irish Horse Sales . Livery . Stud . Shows</p>
    <p class="contact-name">Mark Dabrowski</p>

    <div class="contact-band"></div>
    <p class="contact-lines">
      Email. Twrzap@mailvale.co.uk<br>
      Tel. 07482 936504
    </p>
    <address class="address">
      Birch Lodge<br>
      Carrowmede Lane<br>
      Thistlecombe Lincolnshire LN4 7JX
    </address>
  </main>
</body>
</html>
```